Verno coffee business card

a business card for a cofee van business

similar to the sample business card i am sending
front side with lighter back ground (milky colo or light creamr)
instead of cup please insert my logo
details of business:
email, facebook mobile number (larger fonts)

The back of business card
the bacground is white

the van photo(attached)

this text should be printed (enhance your events with a great coffeevan)

```html
<!DOCTYPE html>
<html lang="en">
<head>
<meta charset="utf-8">
<title>Verno coffee business card</title>
<link rel="stylesheet" href="https://fonts.googleapis.com/css2?family=Oswald:wght@500;600&family=Playball&display=swap">
<style>
  :root {
    --stage: #c9cdcd;
    --linen-light: #e6ddd0;
    --linen-mid: #d2c3ad;
    --linen-dark: #b09a80;
    --espresso: #3a1d12;
    --roast: #6b3a22;
    --bean-light: #8a5232;
    --stain: rgba(120, 70, 40, 0.35);
    --ink: #2e1a12;
    --tagline: #5b1a10;
    --paper: #ffffff;
  }
  * { box-sizing: border-box; margin: 0; padding: 0; }
  html, body { width: 1200px; height: 756px; overflow: hidden; }
  body {
    background: var(--stage);
    position: relative;
    font-family: "Oswald", sans-serif;
  }
  .card {
    position: absolute;
    top: 223px;
    width: 540px;
    height: 309px;
    overflow: hidden;
    box-shadow: 0 6px 18px rgba(0,0,0,0.18);
  }
  .card--front { left: 40px; }
  .card--back { left: 620px; background: var(--paper); }

  .linen-texture {
    position: absolute; inset: 0;
    background: linear-gradient(135deg, var(--linen-dark) 0%, var(--linen-mid) 35%, var(--linen-light) 75%);
  }
  .coffee-rings { position: absolute; inset: 0; }
  .bean-pile { position: absolute; inset: 0; }

  .brand {
    position: absolute;
    left: 70px; top: 68px;
    display: flex; align-items: center; gap: 8px;
  }
  .brand__dot {
    width: 22px; height: 22px; border-radius: 50%;
    background: var(--roast);
  }
  .brand__name {
    font-weight: 600; font-size: 20px;
    color: var(--espresso);
  }

  .owner {
    position: absolute;
    left: 290px; top: 148px;
  }
  .owner__name {
    font-family: "Playball", cursive;
    font-size: 44px;
    color: var(--ink);
    line-height: 1;
    margin-bottom: 12px;
  }
  .contact-list { list-style: none; }
  .contact-list li {
    display: flex; align-items: center; gap: 7px;
    font-weight: 500; font-size: 14px;
    color: var(--ink);
    line-height: 1.5;
  }
  .contact-list svg { width: 12px; height: 12px; flex: none; }

  .van-illustration {
    position: absolute;
    left: 222px; top: 70px;
    width: 96px; height: 70px;
    border-radius: 10px;
    background: linear-gradient(180deg, #a8765a 0%, #6b3a22 100%);
  }
  .tagline {
    position: absolute;
    left: 0; right: 0; top: 158px;
    text-align: center;
    font-weight: 600; font-size: 14px;
    color: var(--tagline);
  }
  .scattered-beans {
    position: absolute;
    right: 36px; bottom: 40px;
    width: 150px; height: 48px;
    border-radius: 24px;
    background: radial-gradient(ellipse at center, #5a2e1a 0%, #8a5232 55%, rgba(255,255,255,0) 75%);
  }
</style>
</head>
<body>

  <section class="card card--front">
    <div class="linen-texture" role="img" aria-label="Light creamy linen sack texture"></div>

    <svg class="coffee-rings" viewBox="0 0 540 309" aria-hidden="true">
      <circle cx="150" cy="30" r="42" fill="none" stroke="var(--stain)" stroke-width="10"/>
      <circle cx="330" cy="110" r="58" fill="none" stroke="var(--stain)" stroke-width="12"/>
      <circle cx="390" cy="205" r="92" fill="none" stroke="rgba(110,55,25,0.55)" stroke-width="14"/>
    </svg>

    <svg class="bean-pile" viewBox="0 0 540 309" role="img" aria-label="Pile of roasted coffee beans">
      <defs>
        <linearGradient id="beanTone" x1="0" y1="0" x2="0" y2="1">
          <stop offset="0" stop-color="var(--bean-light)"/>
          <stop offset="1" stop-color="var(--espresso)"/>
        </linearGradient>
      </defs>
      <path d="M0 160 C60 150 120 152 180 158 C230 165 260 190 300 215 C340 240 370 262 410 275 L420 309 L0 309 Z" fill="url(#beanTone)"/>
    </svg>

    <div class="brand">
      <span class="brand__dot"></span>
      <span class="brand__name">Verno Mobile Café</span>
    </div>

    <div class="owner">
      <h1 class="owner__name">Marcus Hale</h1>
      <ul class="contact-list">
        <li>
          <svg viewBox="0 0 24 24"><path fill="var(--ink)" d="M6.6 10.8a15 15 0 0 0 6.6 6.6l2.2-2.2a1 1 0 0 1 1-.25 11.4 11.4 0 0 0 3.6.6 1 1 0 0 1 1 1V20a1 1 0 0 1-1 1A17 17 0 0 1 3 4a1 1 0 0 1 1-1h3.5a1 1 0 0 1 1 1c0 1.25.2 2.45.6 3.6a1 1 0 0 1-.25 1z"/></svg>
          555-014-2276
        </li>
        <li>
          <svg viewBox="0 0 24 24"><path fill="var(--ink)" d="M2 5h20v14H2z M2 5l10 8 10-8" stroke="var(--linen-light)" stroke-width="1.5"/></svg>
          hello@VernoMobileCafe.com
        </li>
        <li>
          <svg viewBox="0 0 24 24"><circle cx="12" cy="12" r="9" fill="none" stroke="var(--ink)" stroke-width="2"/><path d="M3 12h18M12 3c3 3 3 15 0 18M12 3c-3 3-3 15 0 18" fill="none" stroke="var(--ink)" stroke-width="1.5"/></svg>
          VernoMobileCafe.com
        </li>
      </ul>
    </div>
  </section>

  <section class="card card--back">
    <div class="van-illustration" role="img" aria-label="Illustration of a brown coffee van"></div>
    <p class="tagline">Enhance your events with a great coffeevan</p>
    <div class="scattered-beans" role="img" aria-label="A few scattered coffee beans"></div>
  </section>

</body>
</html>
```